Web page for Gareth Pemblewick Chartered Tax Adviser

I need to take the basic web page that I have created and "Brand it" to be compatible with the corporate logo and stationery created for me by other Studio Flock designers.
I will need a watermark as well as a distinctive home page and then a branded general page for content including a series of Blogs.

Target Market(s)

My practice deals with expatriates including those looking to invest in Australia.

Industry/Entity Type

Crowd

Font styles to use
Other font styles liked:
• Per logo

Requirements
Must have
• Besides the homepage I will need a general page for content, branded in the same style as the letterheads.
Nice to have
• A watermark to go with the blogs and news content.

```html
<!DOCTYPE html>
<html lang="en">
<head>
<meta charset="utf-8">
<title>Gareth Pemblewick – Chartered Tax Adviser</title>
<link rel="stylesheet" href="https://fonts.googleapis.com/css2?family=Cinzel:wght@500;600&family=Lora:ital@1&family=Open+Sans:wght@400;600;700&display=swap">
<style>
  :root {
    --navy: #263f6b;
    --navy-deep: #1f3560;
    --navy-bar: #1c2f55;
    --heading: #1f3b68;
    --text: #5f6266;
    --text-dark: #222;
    --meta: #9aa0a8;
    --rule: #c9ccd3;
    --white: #fff;
  }
  * { box-sizing: border-box; margin: 0; padding: 0; }
  html, body { width: 774px; height: 1200px; overflow: hidden; background: var(--white); }
  body { font-family: "Open Sans", Arial, sans-serif; color: var(--text); }
  .page { position: relative; width: 774px; height: 1200px; overflow: hidden; background: var(--white); }
  .abs { position: absolute; }

  /* Header */
  .header-bg { left: 0; top: 0; width: 774px; height: 120px;
    background: linear-gradient(180deg, #e4e5e8 0%, #f6f6f7 45%, #fff 100%); }
  .brand { left: 48px; top: 17px; display: flex; align-items: center; gap: 7px; }
  .brand-mark { width: 22px; height: 22px; background: var(--navy); border-radius: 3px; }
  .brand-name { font-family: "Cinzel", Georgia, serif; font-weight: 500; color: var(--navy);
    font-size: 14px; line-height: 13px; letter-spacing: .3px; }
  .brand-name small { display: block; font-size: 6.4px; letter-spacing: 1.6px; line-height: 9px; }
  .nav { right: 48px; top: 23px; display: flex; gap: 26px; list-style: none; }
  .nav li { font-size: 8px; font-weight: 600; color: #2b2b2b; letter-spacing: .2px; }

  /* Hero */
  .hero-photo { left: 0; top: 60px; width: 774px; height: 354px;
    background: linear-gradient(135deg, #c9d3df 0%, #eef2f6 35%, #dfe7ef 60%, #8fb2d6 82%, #f0f2f4 100%); }
  .hero-wave { left: 0; top: 40px; }
  .hero-caption { left: 0; top: 375px; width: 486px; height: 72px; background: var(--navy);
    color: var(--white); font-size: 17.5px; line-height: 24px; padding: 10px 0 0 47px; }

  /* Headings */
  .section-title { font-family: "Cinzel", Georgia, serif; font-weight: 600; font-size: 14px;
    color: var(--heading); letter-spacing: .5px; }

  /* Services */
  .services-title { left: 48px; top: 473px; }
  .service-list { top: 500px; list-style: none; font-size: 8.9px; line-height: 16.7px; }
  .service-list li { display: flex; align-items: center; gap: 6px; white-space: nowrap; }
  .tick { width: 9px; height: 8px; flex: none; }
  .service-list.left { left: 48px; }
  .service-list.right { left: 396px; }

  /* Experience band */
  .experience-bg { left: 47px; top: 627px; width: 678px; height: 101px;
    background: linear-gradient(90deg, #f4f4f5 0%, #eceef0 45%, #e2e4e8 75%, #c9ccd1 100%); }
  .experience { left: 63px; top: 640px; width: 650px; }
  .experience h2 { font-size: 17px; font-weight: 700; color: var(--heading); line-height: 22px; }
  .experience p { font-size: 8.6px; line-height: 14.2px; color: var(--text-dark); margin-top: 3px; }

  /* Blog */
  .blog-title { left: 48px; top: 763px; }
  .post { top: 794px; width: 131px; }
  .post-image { width: 131px; height: 85px; border-radius: 3px; }
  .post h3 { font-size: 10.2px; font-weight: 400; color: #2a2a2a; margin-top: 9px; white-space: nowrap; }
  .post .author { font-size: 7.4px; font-weight: 600; color: var(--heading); margin-top: 3px; }
  .post .meta { font-size: 7.4px; color: var(--meta); margin-top: 5px; }
  .post .meta b { font-weight: 400; color: #7d848d; }

  /* Testimonials */
  .testimonials-title { left: 512px; top: 763px; }
  .quote { left: 512px; top: 794px; }
  .quote-text { left: 527px; top: 805px; width: 188px; font-family: "Lora", Georgia, serif;
    font-style: italic; font-size: 8.2px; line-height: 12px; color: #555; }
  .quote-author { right: 48px; top: 895px; text-align: right; font-size: 7.6px; line-height: 13px; }
  .quote-author em { font-family: "Lora", Georgia, serif; color: var(--heading); }
  .quote-author span { display: block; color: var(--text-dark); }

  /* Footer */
  .footer-wave { left: 0; top: 960px; }
  .footer { left: 0; top: 1049px; width: 774px; height: 127px; background: var(--navy); }
  .footer-col { top: 1066px; color: var(--white); }
  .footer-col h4 { font-family: "Cinzel", Georgia, serif; font-weight: 500; font-size: 12px;
    letter-spacing: .4px; margin-bottom: 6px; }
  .footer-col p, .footer-col li { font-size: 8.4px; line-height: 15.6px; list-style: none; }
  .footer-col a { color: var(--white); text-decoration: underline; }
  .footer-about { left: 48px; width: 290px; }
  .footer-links { left: 396px; }
  .footer-contact { left: 569px; }
  .bottom-bar { left: 0; top: 1176px; width: 774px; height: 24px; background: var(--navy-bar);
    color: var(--white); font-size: 7.6px; font-weight: 700; padding: 7px 0 0 48px; letter-spacing: .1px; }
  .social { right: 48px; top: 1181px; display: flex; gap: 3px; }
  .social span { width: 12px; height: 12px; border-radius: 50%; background: var(--white); }
</style>
</head>
<body>
<div class="page">

  <!-- Header -->
  <div class="abs header-bg"></div>
  <div class="abs hero-photo" role="img" aria-label="Photo: adviser's hands over a desk with financial charts and a pen"></div>
  <svg class="abs hero-wave" width="774" height="110" viewBox="0 0 774 110" aria-hidden="true">
    <defs>
      <linearGradient id="headGrad" x1="0" y1="0" x2="0" y2="1">
        <stop offset="0" stop-color="#eeeff1"/><stop offset="1" stop-color="#ffffff"/>
      </linearGradient>
      <linearGradient id="arcGrad" x1="0" y1="0" x2="1" y2="0">
        <stop offset="0" stop-color="#1f3560"/><stop offset="1" stop-color="#2b6a8f"/>
      </linearGradient>
    </defs>
    <path d="M0,0 H774 V44 C690,30 600,38 470,64 C340,92 200,100 0,75 Z" fill="url(#headGrad)"/>
    <path d="M48,60 C150,100 300,92 450,40 C310,82 170,90 48,60 Z" fill="url(#arcGrad)"/>
  </svg>

  <div class="abs brand">
    <span class="brand-mark"></span>
    <span class="brand-name">Gareth Pemblewick<small>CHARTERED TAX ADVISER</small></span>
  </div>
  <ul class="abs nav">
    <li>HOME</li><li>ABOUT</li><li>BLOG</li><li>CONTACT US</li>
  </ul>

  <div class="abs hero-caption">Tax advisers use their knowledge of tax legislation to provide advisory and consultancy services to clients</div>

  <!-- Services -->
  <h2 class="abs section-title services-title">OUR SERVICES</h2>
  <ul class="abs service-list left">
    <li><svg class="tick" viewBox="0 0 9 8"><path d="M1,4.2 L3.4,6.6 L8,1.2" fill="none" stroke="#263f6b" stroke-width="1.8"/></svg>Researching, analysing and interpreting changing tax legislation</li>
    <li><svg class="tick" viewBox="0 0 9 8"><path d="M1,4.2 L3.4,6.6 L8,1.2" fill="none" stroke="#263f6b" stroke-width="1.8"/></svg>Meeting with clients and collating information</li>
    <li><svg class="tick" viewBox="0 0 9 8"><path d="M1,4.2 L3.4,6.6 L8,1.2" fill="none" stroke="#263f6b" stroke-width="1.8"/></svg>Working with tax law and revenue provisions</li>
    <li><svg class="tick" viewBox="0 0 9 8"><path d="M1,4.2 L3.4,6.6 L8,1.2" fill="none" stroke="#263f6b" stroke-width="1.8"/></svg>Preparing and submitting compliance (tax) returns by the deadline</li>
    <li><svg class="tick" viewBox="0 0 9 8"><path d="M1,4.2 L3.4,6.6 L8,1.2" fill="none" stroke="#263f6b" stroke-width="1.8"/></svg>Liaising and negotiating with the National Revenue Office</li>
    <li><svg class="tick" viewBox="0 0 9 8"><path d="M1,4.2 L3.4,6.6 L8,1.2" fill="none" stroke="#263f6b" stroke-width="1.8"/></svg>Providing consultancy services to high value private clients</li>
  </ul>
  <ul class="abs service-list right">
    <li><svg class="tick" viewBox="0 0 9 8"><path d="M1,4.2 L3.4,6.6 L8,1.2" fill="none" stroke="#263f6b" stroke-width="1.8"/></svg>Creating tax strategies for clients and planning their financial futures</li>
    <li><svg class="tick" viewBox="0 0 9 8"><path d="M1,4.2 L3.4,6.6 L8,1.2" fill="none" stroke="#263f6b" stroke-width="1.8"/></svg>Carrying out detailed computations to calculate tax liability</li>
    <li><svg class="tick" viewBox="0 0 9 8"><path d="M1,4.2 L3.4,6.6 L8,1.2" fill="none" stroke="#263f6b" stroke-width="1.8"/></svg>Advising on how to minimise a client's liability</li>
    <li><svg class="tick" viewBox="0 0 9 8"><path d="M1,4.2 L3.4,6.6 L8,1.2" fill="none" stroke="#263f6b" stroke-width="1.8"/></svg>Establishing and structuring family trusts</li>
    <li><svg class="tick" viewBox="0 0 9 8"><path d="M1,4.2 L3.4,6.6 L8,1.2" fill="none" stroke="#263f6b" stroke-width="1.8"/></svg>Estate planning and advising on tax residence and domicile matters</li>
    <li><svg class="tick" viewBox="0 0 9 8"><path d="M1,4.2 L3.4,6.6 L8,1.2" fill="none" stroke="#263f6b" stroke-width="1.8"/></svg>Providing guidance on indirect taxation issues such as VAT</li>
  </ul>

  <!-- Experience band -->
  <div class="abs experience-bg" role="img" aria-label="Faded photo: financial printout with a pen"></div>
  <div class="abs experience">
    <h2>With over 16 years</h2>
    <p>Tax advisers can work in compliance, ensuring a client meets all tax obligations by preparing and submitting tax returns, tax computations and any other necessary forms. Alternatively, they may work in consultancy, advising clients on how to minimise their tax liabilities. Some self-employed tax advisers also offer their clients a range of accountancy services, such as bookkeeping, payroll and VAT.</p>
  </div>

  <!-- Blog -->
  <h2 class="abs section-title blog-title">OUR BLOG</h2>
  <article class="abs post" style="left:47px">
    <div class="post-image" role="img" aria-label="Photo: hands reviewing documents at a meeting table" style="background:linear-gradient(135deg,#6b6f76,#d9dadc 55%,#f2f2f3)"></div>
    <h3>How To Calculate Your Tax</h3>
    <p class="author">from Owen Hartley</p>
    <p class="meta">3 hours ago &nbsp;•&nbsp; 2.341 views</p>
  </article>
  <article class="abs post" style="left:191px">
    <div class="post-image" role="img" aria-label="Photo: colleagues discussing work at a laptop" style="background:linear-gradient(135deg,#3b3f46,#8ea3bd 50%,#cfd6df)"></div>
    <h3>Best Way To Get Advice</h3>
    <p class="author">from Nora Pendell</p>
    <p class="meta">4 hours ago &nbsp;•&nbsp; <b>1.321 views</b></p>
  </article>
  <article class="abs post" style="left:334px">
    <div class="post-image" role="img" aria-label="Photo: adviser and client reviewing paperwork at a desk" style="background:linear-gradient(135deg,#5a5c60,#b9a893 45%,#5f7fae 75%,#dcdfe3)"></div>
    <h3>How To Safe Money</h3>
    <p class="author">from Felix Marrow</p>
    <p class="meta">3 hours ago &nbsp;•&nbsp; <b>1.121 views</b></p>
  </article>

  <!-- Testimonials -->
  <h2 class="abs section-title testimonials-title">CLIENTS’ TESTIMONIALS</h2>
  <svg class="abs quote" width="216" height="101" viewBox="0 0 216 101" aria-hidden="true">
    <path d="M4,0.5 H211 Q215.5,0.5 215.5,5 V81 Q215.5,85.5 211,85.5 H188 L183,95 L168,85.5 H5 Q0.5,85.5 0.5,81 V5 Q0.5,0.5 4,0.5 Z" fill="#fff" stroke="#c9ccd3"/>
  </svg>
  <p class="abs quote-text">Lorem ipsum dolor sit amet, consectetur adipiscing elit, sed do eiusmod tempor incididunt ut labore et dolore magna aliqua. Ut enim ad minim veniam, quis nostrud exercitation ullamco. Lorem ipsum dolor sit amet, consectetur adipi-</p>
  <p class="abs quote-author"><em>Lydia Crestwood</em><span>Director of Harbourline Group</span></p>

  <!-- Footer -->
  <svg class="abs footer-wave" width="774" height="92" viewBox="0 0 774 92" aria-hidden="true">
    <path d="M38,30 C160,56 300,54 440,34 C570,14 680,14 734,34" fill="none" stroke="#b8bbc4" stroke-width="3.5" stroke-linecap="round"/>
    <path d="M0,58 C120,88 260,86 410,62 C550,40 680,30 774,40 V92 H0 Z" fill="#263f6b"/>
  </svg>
  <div class="abs footer"></div>

  <div class="abs footer-col footer-about">
    <h4>ABOUT GARETH PEMBLEWICK SERVICES</h4>
    <p>Vivamus non elementum enim. Vestibulum fringilla placerat vestibulum. Donec consequat scelerisque lorem, quis laoreet tortor dapibus nec. Duis sodales quis odio quis pretium. Etiam auctor sollicitudin enim. Duis tempus semper sodales. Duis sodales quis odio quis pretium.</p>
  </div>
  <div class="abs footer-col footer-links">
    <h4>USEFUL LINKS</h4>
    <ul>
      <li><a href="#">About Us</a></li>
      <li><a href="#">Services</a></li>
      <li><a href="#">Blog</a></li>
      <li><a href="#">Testimonials</a></li>
    </ul>
  </div>
  <div class="abs footer-col footer-contact">
    <h4>CONTACT US</h4>
    <p>PO BOX 418273</p>
    <p>Brookhaven, QL 40211-3158</p>
    <p>(015) 2846 3917</p>
    <p>info@garethpemblewick.com</p>
  </div>

  <div class="abs bottom-bar">GARETH PEMBLEWICK (C) COPYRIGHT 2014. ALL RIGHTS RESERVED</div>
  <div class="abs social" aria-label="Social links">
    <span></span><span></span><span></span><span></span><span></span>
  </div>

</div>
</body>
</html>
```